Courtside Heritage Trust Web site

We need a Wordpress web site for a new non-profit, the Courtside Heritage Trust. CHT's mission is to raise the awareness of sustainability within the tennis community and industry worldwide. Our focus is on education and being a catalyst in connecting expertise in the environmental field with tennis organizations to create sustainable change. Our primary targets are youth education and empowerment, tennis facility management, and Celebrity tennis players' engagement.

The design needs to be elegant and attractive to potential corporate donors and reflect the high level of sophistication of the tennis demographic. It needs to be very graphic with high-impact photos and the ability to inspire action. Although it can be simple now it will need to have the capability of expanding to allow acceptance of donations online, offering of information products in exchange for email registration, and potentially a membership-oriented section of the site with forums and community engagement.

At the present time, it is more of an information-oriented site that tells a compelling story and inspires people to take action to get involved in the way that most fits their needs.

We need to have the ability to add pages and blog posts easily on our own while maintaining a relationship that would allow us a cost-effective way of making more major additions and adjustments to the site.

Attached is our logo. Thanks for your desire to help us make an impact on the world.

Industry/Entity Type

Graphic Design

```html
<!DOCTYPE html>
<html lang="en">
<head>
<meta charset="utf-8">
<title>Courtside Heritage Trust</title>
<link href="https://fonts.googleapis.com/css2?family=Open+Sans:ital,wght@0,400;0,600;0,700;1,400&display=swap" rel="stylesheet">
<style>
:root{
  --brand:#0f6089;
  --brand-dark:#0b4f73;
  --accent:#13a4e0;
  --text:#333;
  --muted:#555;
  --rule:#cfcfcf;
  --panel:#e6e6e6;
  --footer:#e4e3e3;
  --hero-warm:#b98a52;
  --hero-mid:#6d6f74;
  --hero-cool:#2a3f58;
  --white:#fff;
}
*{margin:0;padding:0;box-sizing:border-box}
html,body{width:846px;height:1200px;overflow:hidden;background:var(--white)}
body{font-family:"Open Sans",Arial,sans-serif;color:var(--text);position:relative}
.abs{position:absolute}
.top-band{left:0;top:0;width:846px;height:6px;background:var(--brand)}
.brand{left:80px;top:61px;display:flex;align-items:center;gap:6px;color:var(--brand);font-size:12.5px;font-weight:400;letter-spacing:.4px;white-space:nowrap}
.brand-dot{width:8px;height:8px;border-radius:50%;background:var(--brand)}
.lang{left:566px;top:19px;font-size:8px;color:var(--muted);display:flex;align-items:center;gap:4px}
.flag{width:14px;height:9px;background:#2c4a8a}
.search{left:620px;top:14px;width:134px;height:20px;background:#efefef}
.search svg{position:absolute;right:6px;top:4px}
.nav{left:294px;top:62px;display:flex;height:28px;font-size:10px;color:var(--muted)}
.nav a{display:block;padding:0 7px;line-height:28px;text-decoration:none;color:inherit}
.nav a.active{background:var(--brand);color:var(--white);padding:0 8px}
.header-rule{left:0;top:90px;width:846px;height:2px;background:var(--brand)}
.hero{left:0;top:92px;width:846px;height:325px;background:linear-gradient(90deg,var(--hero-warm) 0%,var(--hero-mid) 40%,var(--hero-cool) 100%)}
.hero-copy{left:408px;top:214px;color:var(--white);text-transform:uppercase;line-height:1}
.hero-copy span{display:block;white-space:nowrap}
.hero-copy .l1{font-size:12px;margin-bottom:2px}
.hero-copy .l2{font-size:14.5px;margin-bottom:1px}
.hero-copy .l3{font-size:23.5px;margin-bottom:0}
.hero-copy .l4{font-size:16.8px}
.hero-more{left:408px;top:294px;font-size:9px;color:var(--accent);text-transform:uppercase}
.dots{left:396px;top:388px;display:flex;gap:9px}
.dots span{width:6px;height:6px;background:#a8b0b8}
.dots span.on{background:var(--brand)}
.intro-title{left:0;top:437px;width:846px;text-align:center;font-size:16px;color:var(--brand);font-weight:400}
.intro-title b{font-weight:700}
.intro-text{left:102px;top:476px;width:642px;text-align:center;font-size:9.2px;line-height:11.3px;color:var(--muted)}
.read-link{font-style:italic;color:var(--brand);font-size:9px}
.rule{height:1px;background:var(--rule);left:105px;width:636px}
.join-photo{left:112px;top:604px;width:310px;height:132px;background:linear-gradient(135deg,#8a8a8a,#bdbdbd 50%,#6e6e6e)}
.join-panel{left:112px;top:736px;width:310px;height:88px;background:var(--panel)}
.join-band{left:350px;top:736px;width:72px;height:32px;background:var(--brand-dark)}
.join-tag{left:184px;top:725px;width:166px;height:31px;background:var(--brand);color:var(--white);font-size:14px;font-weight:600;text-align:center;line-height:31px}
.join-text{left:128px;top:775px;width:280px;font-size:9px;line-height:11px;color:var(--muted)}
.join-more{left:364px;top:805px}
.col-divider{left:447px;top:606px;width:1px;height:220px;background:var(--rule)}
.blog-title{left:473px;top:600px;font-size:15px;color:var(--brand);font-weight:400}
.blog-title b{font-weight:700}
.blog-rule{left:473px;width:266px;height:1px;background:var(--rule)}
.thumb{width:68px;height:54px}
.thumb-racket{background:linear-gradient(135deg,#1d5f9a,#5aa4d8)}
.thumb-court{background:linear-gradient(180deg,#7fa56a 0%,#2f7a5a 45%,#3d8a6a 100%)}
.post-date{font-size:9px;font-weight:700;color:var(--text)}
.post-title{font-size:9px;font-weight:700;color:var(--text)}
.post-text{font-size:9px;color:var(--text);line-height:11px}
.news{left:106px;top:880px;width:316px;height:103px;background:var(--panel)}
.news h3{position:absolute;left:16px;top:12px;font-size:12px;font-weight:600;color:var(--text)}
.news .date{position:absolute;left:16px;top:34px;font-size:9px;font-weight:700;color:var(--brand)}
.news p{position:absolute;left:16px;top:46px;width:290px;font-size:9px;line-height:11px;color:var(--muted)}
.arrows{position:absolute;left:244px;top:78px;display:flex;gap:2px}
.arrows span{width:18px;height:16px;background:var(--white);color:#999;font-size:9px;text-align:center;line-height:16px}
.donate{left:474px;top:880px;width:266px;height:103px;background:var(--brand)}
.donate .lead{position:absolute;left:0;top:18px;width:266px;text-align:center;color:var(--white);font-size:11px;line-height:14px}
.donate .lead b{font-size:14.5px}
.donate .btn{position:absolute;left:93px;top:54px;width:81px;height:28px;background:var(--accent);color:var(--white);font-size:11px;font-weight:700;text-align:center;line-height:28px}
.footer{left:0;top:1010px;width:846px;height:160px;background:var(--footer)}
.fcol{top:1044px}
.fcol h4{font-size:11.5px;font-weight:600;color:var(--brand);margin-bottom:6px}
.fcol li{list-style:none;font-size:7.8px;line-height:9.4px;color:var(--muted);text-transform:uppercase}
.footer-divider{left:522px;top:1034px;width:1px;height:106px;background:#9fb5c3}
.sub-title{left:546px;top:1043px;font-size:12px;color:var(--brand)}
.sub-input{left:546px;top:1072px;width:208px;height:26px;background:var(--white);font-size:8.5px;font-style:italic;color:#888;padding:7px 12px}
.sub-btn{left:686px;top:1102px;width:68px;height:22px;background:var(--brand-dark);color:var(--white);font-size:10px;text-align:center;line-height:22px}
.bottom-band{left:0;top:1170px;width:846px;height:30px;background:var(--brand)}
.social{left:93px;top:1177px;display:flex;gap:7px}
.social span{width:16px;height:16px;border-radius:50%;background:#0a3e5c}
.copyright{left:572px;top:1180px;font-size:7.8px;color:var(--white);text-transform:uppercase}
</style>
</head>
<body>
<div class="abs top-band"></div>

<header>
  <div class="abs brand"><span class="brand-dot"></span>COURTSIDE HERITAGE TRUST</div>
  <div class="abs lang"><span class="flag"></span>ENG ▾</div>
  <div class="abs search">
    <svg width="12" height="12" viewBox="0 0 12 12"><circle cx="5" cy="5" r="3.6" fill="none" stroke="#aaa" stroke-width="1.4"/><line x1="7.6" y1="7.6" x2="11" y2="11" stroke="#aaa" stroke-width="1.6"/></svg>
  </div>
  <nav class="abs nav">
    <a class="active">HOME</a><a>COMPELLING STORIES</a><a>MEMBERS ZONE</a><a>DONATIONS</a><a>BLOG</a><a>FORUMS</a><a>CONTACT US</a>
  </nav>
  <div class="abs header-rule"></div>
</header>

<section>
  <div class="abs hero" role="img" aria-label="Hero photograph: close-up of a tennis ball on a court at sunset"></div>
  <div class="abs hero-copy">
    <span class="l1">Our mission is to raise the awareness</span>
    <span class="l2">of sustainability within the</span>
    <span class="l3">Tennis community</span>
    <span class="l4">and industry worldwide.</span>
  </div>
  <div class="abs hero-more">Know more</div>
  <div class="abs dots"><span class="on"></span><span></span><span></span><span></span></div>
</section>

<section>
  <h2 class="abs intro-title">WHAT IS <b>COURTSIDE HERITAGE TRUST ?</b></h2>
  <p class="abs intro-text">Today, Riverside Green Links Programme fondly known as RGLP is based across a number of community centres in our town. The original project opened for operation in The Meadows, then service support expanded into our Ashford Terrace Centre, followed by further investment to open Elm Hollow Community Centre, providing a one stop shop solution to meet our changing community needs, from confidential support services for anyone dealing with drugs or alcohol problems, through to educational training, job search and community outreach programme.<br><br><span class="read-link">Read more</span></p>
  <div class="abs rule" style="top:576px"></div>
</section>

<section>
  <div class="abs join-photo" role="img" aria-label="Grid of black and white portraits of members"></div>
  <div class="abs join-panel"></div>
  <div class="abs join-band"></div>
  <div class="abs join-tag">BE PART OF CHT</div>
  <p class="abs join-text">This innovative program creates individual member savings<br>Find out how you can be part of Legacy 2014.</p>
  <span class="abs read-link join-more">Know more</span>

  <div class="abs col-divider"></div>

  <h2 class="abs blog-title">LATEST <b>BLOG FEEDS</b></h2>
  <div class="abs blog-rule" style="top:625px"></div>

  <div class="abs thumb thumb-racket" style="left:474px;top:634px" role="img" aria-label="Tennis racket hitting a ball"></div>
  <div class="abs post-date" style="left:552px;top:633px">23/February/2014</div>
  <div class="abs post-title" style="left:554px;top:651px">Emotional Intelligence</div>
  <div class="abs post-text" style="left:554px;top:662px">Click here to see Claire's Brandline Article.</div>
  <span class="abs read-link" style="left:694px;top:680px">Read More</span>
  <div class="abs blog-rule" style="top:696px"></div>

  <div class="abs post-date" style="left:474px;top:707px">11/January/2014</div>
  <div class="abs post-text" style="left:474px;top:724px">* Creativity Training dates available in August<br>* Moderator Boot Camp dates available in June and August!</div>
  <div class="abs blog-rule" style="top:759px"></div>

  <div class="abs thumb thumb-court" style="left:474px;top:769px" role="img" aria-label="Outdoor tennis court surrounded by trees"></div>
  <div class="abs post-date" style="left:552px;top:768px">23/February/2014</div>
  <div class="abs post-title" style="left:554px;top:786px">Emotional Intelligence</div>
  <div class="abs post-text" style="left:554px;top:797px">Click here to see Claire's Brandline Article.</div>
  <span class="abs read-link" style="left:692px;top:815px">Read More</span>

  <div class="abs rule" style="top:857px"></div>
</section>

<section>
  <div class="abs news">
    <h3>News Updates</h3>
    <div class="date">11/January/2014</div>
    <p>Creativity Training dates available in August Moderator Boot Camp dates available in June and August!</p>
    <div class="arrows"><span>‹</span><span>›</span></div>
    <svg style="position:absolute;right:0;bottom:0" width="26" height="26" viewBox="0 0 26 26"><polygon points="26,0 26,26 0,26" fill="#fff"/><polygon points="26,0 0,26 0,0" fill="#0f6089"/></svg>
  </div>
  <div class="abs donate">
    <div class="lead">Make a Donation<br>to the <b>COURTSIDE HERITAGE TRUST</b></div>
    <div class="btn">DONATE</div>
    <svg style="position:absolute;right:0;bottom:0" width="26" height="26" viewBox="0 0 26 26"><polygon points="26,0 26,26 0,26" fill="#fff"/><polygon points="26,0 0,26 2,2" fill="#d6d6d6"/></svg>
  </div>
</section>

<footer>
  <div class="abs footer"></div>
  <div class="abs fcol" style="left:94px"><h4>ABOUT US</h4><ul><li>Services</li><li>What we do</li><li>Our staff &amp; board</li><li>Our work with CHT</li><li>Volunteer</li><li>Corporate donors</li><li>Events</li></ul></div>
  <div class="abs fcol" style="left:208px"><h4>DONATE</h4><ul><li>How to donate</li><li>Why I donate</li><li>Our donors</li><li>Monthly giving</li><li>Publications</li><li>FAQ</li><li>Support</li></ul></div>
  <div class="abs fcol" style="left:323px"><h4>CONTACT CHT</h4><ul><li>Sample address</li><li>400-118 Harbour Street</li><li>Millbrook ON, London</li><li>K4R 1M8</li><li>5550142236 Ext. 210</li><li>TF 1-800-555-0199 Ext. 210</li><li>INFO@CHTSAMPLE</li></ul></div>
  <div class="abs footer-divider"></div>
  <div class="abs sub-title">Subscribe newsletter</div>
  <div class="abs sub-input">enter your mail address</div>
  <div class="abs sub-btn">SUBMIT</div>
  <div class="abs bottom-band"></div>
  <div class="abs social"><span></span><span></span><span></span></div>
  <div class="abs copyright">Copyright 2014 CHT. All rights are reserved</div>
</footer>
</body>
</html>
```